依頼詳細
★重視する点
60歳~70歳の社長が読むものです。
商品も50万円以上のコンサルティングなので、
信頼感、安心感を与える雰囲気を重視します。
また、高級感のあるイメージも重要です。

★ページ構成について
表面 キャッチ
中面 スキームの説明、Q&A
裏面 報酬、お問合せ先

内容を詰めることができれば、
A4裏表の1枚でもOKです。
(むしろ、そうできればベストです)

★文章の修正について
必要があれば文章やタイトルの修正もOKです。
目的は、
「このような方法があるなら、もっと話しを聞いてみたい」
と思わせることです。
そのように思わせるものであれば、
タイトルや文章の修正も歓迎します。

★お問合せの部分について
数名でこのパンフを共同利用する予定です。
ですから、お問合せの部分は
各自の住所と会社名、電話番号、メールアドレスなどが
入りますので、そのようなスペースを空けておいてください。

★利用用途
このパンフレットは、
問合せがあった人に、最初の相談の時、お渡しします。
またセミナーなど開催したときに、資料としてお渡しします。

★納品形式について
イラストレーターV14で開ける形式でお願いいたします。
また、JpegやPNGもお願いします。
サイズ
A4
ページ数
4ページ
希望イメージ
シンプル 複雑
単色 カラフル
暗い 明るい
日常 高級
遊び心 厳粛
未来的 伝統的
女性的 男性的
希望する色
茶系、グレー系
納品ファイル
• 高解像度JPG (.jpg)
• イラストレーター形式 (.ai)
• PNG形式 (.png)
補足説明
・表面、中面、裏面のラフ案をご提案ください。
こちらの希望するイメージに近い提案を1つ選択させて頂きます。

・希望に近づけるために、修正要望を個別にさせていただくこともあります。
コンペ方式のため、修正後に当選されない場合も、どうかご了承ください。
参加報酬は4件用意していますので、
なるべくそちらで対応するようにいたします。

・今後も同様なものを作成する予定です。
依頼は今回だけではなく、こちらの求める条件に合えば
継続して依頼したいと思います。

・疑問点などございましたらお気軽にご質問ください。
早速に1件のご提案があり、大変ありがとうございます。
さすがプロの方のデザインはすばらしく、
これからの提案もとても期待しております。

★お願い スキームの図解もデザインに盛り込んでください

原案に、自社株信託のスキームの図解がありますが、
できれば、パンフレットにも図解を盛り込んで
いただけないでしょうか?
もちろん、原案のスキームの図を参考に
あなたのイメージするようにデザインし直していただきたいです。

原案がワードで作成したため、マクロウィルスなどご心配の方も
いらっしゃると思いますので、原案のPDFを添付します。
また、スキームの図のPNGも添付します。
図はMSのVisioというソフトで作っております。
開ける人は少ないでしょうが、そのファイルも添付します。
■ 選んだ理由

ビジネスというジャングルを駆け巡る獅子(社長)が
寂しげな目で「引退するか」という表紙は、
提案の中で、圧倒的でした。

また、多くの提案をいただいて、気づいたのですが、
老夫婦だと保険の勧誘、引退をイメージする物だと
投資信託などの金融商品の勧誘のような印象を与えることがわかり、
ライオンの表紙はそのような印象も与えないので、
当選とさせていただきました。

■ 提案者全員のお礼・コメント

多くの方からご応募いただき、誠にありがとうございました。
どの提案も、とても私のような素人ではできない
優れたデザインだったと思います。
さすがプロの仕事を見せていただきました。
また、今後も提案をお願いすると思いますが、
そのときも、よろしくお願いいたします。

この度は大変ありがとうございました。

```html
<!DOCTYPE html>
<html lang="ja">
<head>
<meta charset="utf-8">
<title>社長！そろそろ「隠居」しませんか？</title>
<link href="https://fonts.googleapis.com/css2?family=Noto+Serif+JP:wght@400;600;700;900&display=swap" rel="stylesheet">
<style>
:root{
  --bg-dark:#2b2019;
  --bg-mid:#4a3a2d;
  --panel:#d9d0c3;
  --panel-box:#f4f0ea;
  --accent:#c2611c;
  --ink:#2a211b;
  --white:#ffffff;
  --list-bg:#3a2e25;
}
*{margin:0;padding:0;box-sizing:border-box}
html,body{width:849px;height:1200px;overflow:hidden}
body{font-family:"Noto Serif JP",serif;color:var(--ink);background:var(--bg-dark)}
.page{position:relative;width:849px;height:1200px;overflow:hidden;
  background:radial-gradient(ellipse at 70% 25%,var(--bg-mid) 0%,var(--bg-dark) 70%)}
.portrait{position:absolute;left:390px;top:560px;width:459px;height:640px;
  background:linear-gradient(180deg,rgba(40,32,26,0) 0%,#1e1814 35%,#15110e 100%)}
.headline{position:absolute;top:16px;right:22px;height:480px;writing-mode:vertical-rl;
  font-weight:900;font-size:72px;line-height:1.1;color:var(--white);letter-spacing:0;
  text-shadow:0 2px 6px rgba(0,0,0,.5)}
.headline .key{color:var(--accent);background:var(--white);padding:6px 0}
.badge{position:absolute;left:620px;top:930px;width:150px;height:150px;border-radius:50%;
  background:#3d3129;border:2px solid #6b5848;display:flex;align-items:center;justify-content:center;
  color:var(--white);font-size:11.5px;line-height:1.8;text-align:center;padding:14px;font-weight:600}
.panel{position:absolute;left:42px;top:112px;width:330px;height:1022px;background:var(--panel);
  padding:12px;display:flex;flex-direction:column;gap:12px}
.box{background:var(--panel-box);padding:12px 13px}
.lead{color:var(--accent);font-weight:900;font-size:15px;line-height:1.5;margin-bottom:8px}
.body{font-size:10.6px;line-height:1.95}
.body p{margin-bottom:5px}
.option{font-weight:700;font-size:11px;margin-top:3px;margin-bottom:0 !important}
.features{background:var(--list-bg);color:var(--white);padding:14px 16px;font-size:11.5px;line-height:1.95}
.features li{list-style:none;display:flex;gap:8px;align-items:flex-start}
.features svg{flex:none;margin-top:6px}
.features .tail{margin-top:2px}
</style>
</head>
<body>
<div class="page">
  <div class="portrait" role="img" aria-label="スーツ姿の経営者の後ろ姿の写真"></div>

  <h1 class="headline">社長！<br>そろそろ<br><span class="key">「隠居」</span><br>しませんか？</h1>

  <div class="badge">贈与税をかけずに、<br>会社の株を後継者に<br>渡す方法があるんです。</div>

  <section class="panel">
    <div class="box">
      <p class="lead">後継者も決まったし、そろそろ「隠居」したい。しかし、株の譲渡には多額の税金がかかる…</p>
      <div class="body">
        <p>会社のオーナーであるあなたも60代、70代になり、そろそろ引退（隠居）を考える年齢ではありませんか。会社の株は年々価値が上がり、そのまま後継者へ渡そうとすると、多額の税金が発生します。長年育ててきた会社だからこそ、「事業承継」は避けて通れない課題です。では株をどのように後継者へ渡せばよいのでしょうか。</p>
        <p class="option">○タダで譲す</p>
        <p>多額の贈与税（株価が3000万円なら1200万円以上の贈与税）がかかります。</p>
        <p class="option">○買い取ってもらう</p>
        <p>後継者が多額の買取資金を用意しなければならず、会社や個人の資金繰りを圧迫することになります。</p>
        <p>また、株を渡してしまうと、後継者が経営に失敗したり、思うように育たなかったりしても、元に戻すことはできません。遺言で渡す方法もありますが、相続時まで経営の実権を移すことができず、争いの種を残すこともあります。株価や税制は年々変わるため、早めの準備が何より大切です。</p>
      </div>
    </div>

    <div class="box">
      <p class="lead">贈与税もかからず、遺言も不要。<br>しかもいつでも元に戻せる方法があるの!?</p>
      <div class="body">
        <p>生前贈与でも、遺言でもない「第三の方法」があります。それが「自社株信託」という仕組みです。株式を信託することで、経営権だけを後継者に移し、財産としての株はオーナーの手元に残すことができます。この仕組みを活用すれば、次のような特徴があります。</p>
      </div>
    </div>

    <ul class="features">
      <li><svg width="10" height="10" viewBox="0 0 10 10"><rect width="10" height="10" fill="#c2611c"/></svg>贈与税がかからない</li>
      <li><svg width="10" height="10" viewBox="0 0 10 10"><rect width="10" height="10" fill="#c2611c"/></svg>買い取り資金も不要</li>
      <li><svg width="10" height="10" viewBox="0 0 10 10"><rect width="10" height="10" fill="#c2611c"/></svg>後継者が不適切なら、株式を返してもらえる。</li>
      <li><svg width="10" height="10" viewBox="0 0 10 10"><rect width="10" height="10" fill="#c2611c"/></svg>そのときも新たな贈与税や買い取り資金は不要</li>
      <li><svg width="10" height="10" viewBox="0 0 10 10"><rect width="10" height="10" fill="#c2611c"/></svg>遺言の方式によらなくてもよい</li>
      <li class="tail">などの特徴があります。</li>
    </ul>
  </section>
</div>
</body>
</html>
```